Baby Muslin Wrap/Swaddle Box Packaging Design

We are a company that sells baby muslin wraps. We currently sell cotton and bamboo baby muslin wraps in egdy, monochrome designs. We are looking for new packaging designs and would like this new packaging to consist of a box with a window at the front to see and feel muslin wrap. Each box will hold one wrap (please see some examples of style of box we are after attached). Our logo (Ned and Posy) should be on the front of the box. We are open to any colour options/illustrations on the box but would like it to stand out if placed on a shelf in a store. We would be interested in seeing a white box with monochrome designs across box.. Gold writing would also be great to see. There will be some additional info that will need to go on the back of the box.
Target Market(s)
women 20-40 year of age.
Industry/Entity Type
Baby
Requirements
Must have
- Logo
- Box design with window

```html
<!DOCTYPE html>
<html lang="en">
<head>
<meta charset="utf-8">
<title>Ned and Posy – Bamboo Muslin Swaddle Box</title>
<link rel="stylesheet" href="https://fonts.googleapis.com/css2?family=Amatic+SC:wght@400;700&display=swap">
<style>
  :root {
    --page: #ffffff;
    --kraft: #c99a6c;
    --ink: #1a1512;
    --cut: #111111;
    --fold: #ffffff;
    --window: #ffffff;
    --hole: #5c4a1e;
  }
  * { margin: 0; padding: 0; box-sizing: border-box; }
  html, body {
    width: 1200px; height: 1162px; overflow: hidden; background: var(--page);
  }
  .canvas {
    position: relative; width: 1200px; height: 1162px; overflow: hidden;
  }
  .dieline {
    position: absolute; left: 0; top: 0;
    width: 1050px; height: 1017px;
    transform: scale(1.142857); transform-origin: 0 0;
    font-family: "Amatic SC", cursive;
    color: var(--ink);
  }
  .dieline > .box-shape { position: absolute; left: 0; top: 0; }
  .box-body { fill: var(--kraft); stroke: var(--cut); stroke-width: 2; stroke-linejoin: miter; }
  .fold { stroke: var(--fold); stroke-width: 1; stroke-dasharray: 6 4; fill: none; }
  .window { fill: var(--window); }
  .hang-hole { fill: var(--hole); stroke: #2c220e; stroke-width: 1; }
  .dots { stroke: var(--ink); stroke-width: 4; stroke-dasharray: 4 6; }

  .front-brand {
    position: absolute; left: 120px; top: 340px; width: 174px;
    display: flex; align-items: center; justify-content: center; gap: 6px;
    font-weight: 700; font-size: 28px; line-height: 1; white-space: nowrap;
  }
  .front-brand .brand-dot {
    width: 12px; height: 12px; border-radius: 50%; background: var(--ink); flex: none;
  }
  .front-title {
    position: absolute; left: 100px; top: 752px; width: 213px;
    text-align: center; font-size: 25px; letter-spacing: 0.5px; line-height: 30px;
    white-space: nowrap;
  }

  .back-panel {
    position: absolute; left: 508px; top: 322px; width: 244px;
    text-align: center;
  }
  .back-panel .headline { font-weight: 700; font-size: 23px; line-height: 21px; letter-spacing: 1px; }
  .back-panel .intro { margin-top: 16px; font-size: 15px; line-height: 16px; font-weight: 700; letter-spacing: 0.5px; }
  .back-panel .feature-title {
    margin-top: 20px; font-size: 11px; font-weight: 700; text-decoration: underline; letter-spacing: 0.5px;
  }
  .back-panel .feature-text { margin-top: 3px; font-size: 9.5px; line-height: 11px; font-weight: 700; }
  .back-panel .divider { position: static; margin: 14px auto 0; width: 48px; height: 8px; display: block; }
  .back-panel .online { margin-top: 10px; font-size: 15px; font-weight: 700; }
  .back-panel .web { font-size: 22px; font-weight: 700; line-height: 26px; }
  .social { list-style: none; margin: 4px auto 0; width: 180px; text-align: left; }
  .social li {
    display: flex; align-items: center; gap: 8px;
    font-size: 14px; font-weight: 700; line-height: 18px; white-space: nowrap;
  }
  .social .social-mark { width: 14px; height: 14px; border-radius: 2px; background: var(--ink); flex: none; }
</style>
</head>
<body>
<main class="canvas">
  <div class="dieline">
    <svg class="box-shape" width="1050" height="1017" viewBox="0 0 1050 1017" aria-hidden="true">
      <path class="box-body" d="M71,105 L86,65 L327,65 L341,105 L341,262 L371,162 L484,162 L498,262 L618,262 A12,12 0 0 0 642,262 L768,262 L781,162 L894,162 L922,262 L978,290 L978,800 L922,830 L922,927 L824,927 L848,907 L768,830 L768,957 L722,957 L722,907 L540,907 L540,957 L498,957 L498,830 L419,907 L441,927 L341,927 L341,830 L286,907 L300,957 L113,957 L128,907 L71,830 Z"/>
      <line class="fold" x1="71" y1="105" x2="341" y2="105"/>
      <line class="fold" x1="71" y1="262" x2="922" y2="262"/>
      <line class="fold" x1="71" y1="830" x2="922" y2="830"/>
      <line class="fold" x1="341" y1="262" x2="341" y2="830"/>
      <line class="fold" x1="498" y1="262" x2="498" y2="830"/>
      <line class="fold" x1="768" y1="262" x2="768" y2="830"/>
      <line class="fold" x1="922" y1="262" x2="922" y2="830"/>
      <rect class="window" x="100" y="430" width="213" height="302" rx="10"/>
      <circle class="hang-hole" cx="421" cy="346" r="9"/>
      <circle class="hang-hole" cx="845" cy="346" r="9"/>
      <line class="dots" x1="100" y1="748" x2="313" y2="748"/>
      <line class="dots" x1="100" y1="783" x2="313" y2="783"/>
    </svg>

    <div class="front-brand"><span class="brand-dot"></span>Ned and Posy</div>
    <p class="front-title">Bamboo Muslin Swaddle</p>

    <section class="back-panel">
      <h1 class="headline">Made from 100% bamboo<br>47" x 47" ~ 120cm x 120cm</h1>
      <p class="intro">Stimulate baby's eyesight and brain<br>development with this high-contrast<br>black and white muslin swaddle.</p>
      <h2 class="feature-title">Breathable</h2>
      <p class="feature-text">Bamboo rayon has anti-bacterial qualities which<br>makes it perfect for baby. It also has temperature<br>regulating properties, which helps reduce the risk of overheating<br>while keeping your bubba warm in winter and cool in summer!</p>
      <h2 class="feature-title">Versatile</h2>
      <p class="feature-text">Works as a pram or breastfeeding cover, changing pad cover,<br>swaddle, scarf sarong, burp cloth, light shade,<br>tummy time blanket and more.</p>
      <svg class="divider" viewBox="0 0 48 8" aria-hidden="true"><path d="M0,4 L18,4 M30,4 L48,4" stroke="#1a1512" stroke-width="1.5"/><ellipse cx="24" cy="4" rx="3" ry="3.5" fill="#1a1512"/></svg>
      <p class="online">We're online!</p>
      <p class="web">www.NedAndPosy.com.au</p>
      <ul class="social">
        <li><span class="social-mark"></span>friendsbook.example/nedandposy</li>
        <li><span class="social-mark"></span>@nedandposybaby</li>
        <li><span class="social-mark"></span>pinboard.example/nedandposy</li>
      </ul>
      <svg class="divider" viewBox="0 0 48 8" aria-hidden="true"><path d="M0,4 L18,4 M30,4 L48,4" stroke="#1a1512" stroke-width="1.5"/><ellipse cx="24" cy="4" rx="3" ry="3.5" fill="#1a1512"/></svg>
    </section>
  </div>
</main>
</body>
</html>
```